Website Design for Non-profit

We are looking for a new site design for the Patrons of the Northern Heritage Hall. The current site can be found at
http://www.patrons-hall.org/pnhhindex_e.html
The URL is provided for reference. We want a completely different look and layout which is shown in the specifications document. Visiting the site, you can learn more about the organization.
Initially, we would like a home page, and inside page provided. Once we a home page and inside page are selected, we would like a simple mobile template provided.
I have attached a full description of the project as well as the specifications document and a zip file containing images for the site.
As mentioned in the specs document, we want to include an image of the museum in the header. The zip file is too large for us to upload (80 meg). The zip file can be obtained by clicking this link:
http://qzl.cc/TrWpKe
The zip file contains several exterior photos and you can select the one you feel is most appropriate to your design.
Reason: A long weekend is coming up and a few members of the team are unavailable for review.
Reason: Reviewing designs. Should have a decision next week.
Reason: We are discussing the designs and looking to reach a consensus. I will be implementing some designs today or tomorrow. Hopefully final selection will be next week.
Reason: Still reviewing designs. Hope to get a decision soon.
Reason: Working to finalize the design. Very close.
Industry/Entity Type
Museum
Look and feel
Each slider illustrates characteristics of the customer's brand and the style your logo design should communicate.

```html
<!DOCTYPE html>
<html lang="en">
<head>
<meta charset="utf-8">
<title>Patrons of the Northern Heritage Hall</title>
<link rel="stylesheet" href="https://fonts.googleapis.com/css2?family=Arimo:wght@400;700&family=Kalam:wght@400;700&family=Great+Vibes&family=Amaranth&display=swap">
<style>
:root{
  --lime:#b9d65e;
  --lime-light:#d3e78f;
  --lime-pale:#e9f3c6;
  --green:#4f7f24;
  --green-dark:#3b6519;
  --text:#666;
  --muted:#999;
  --orange:#f5a31b;
  --red:#c8141b;
  --sky:#5aa9d6;
  --grey:#ececec;
  --white:#fff;
}
*{box-sizing:border-box;margin:0;padding:0}
html,body{width:745px;height:1200px;overflow:hidden}
body{font-family:"Arimo",Arial,sans-serif;color:var(--text);background:var(--white)}
.canvas{position:relative;width:745px;height:1200px;overflow:hidden}
.abs{position:absolute}
.header{left:0;top:0;width:745px;height:98px;background:linear-gradient(180deg,#c6de74,var(--lime))}
.hero-band{left:0;top:98px;width:745px;height:332px;background:var(--grey)}
.live-help{left:98px;top:18px;width:148px;height:40px;border:2px solid var(--lime-light);border-radius:4px;background:#c3dc6e;display:flex;align-items:center;gap:6px;padding-left:10px;color:var(--white);font-family:"Great Vibes",cursive;font-size:17px}
.brand{display:flex;align-items:center;gap:6px;color:#222;font-weight:700;font-size:10px;line-height:12px}
.brand-mark{width:14px;height:14px;background:var(--green-dark)}
.top-links{left:528px;top:10px;list-style:none;font-size:6.5px;color:#555;line-height:15.4px}
.top-links li::before{content:"› ";}
.social{width:26px;height:26px;border-radius:50%;background:var(--lime-pale);border:2px solid #dfeeb0}
.ribbon{top:92px;height:24px;background:linear-gradient(180deg,#5f922c,var(--green-dark));color:var(--white);font-weight:700;font-size:8px;display:flex;align-items:center;gap:10px}
.search{left:252px;top:79px;width:241px;height:27px;background:var(--green);padding:4px 6px;display:flex;gap:6px}
.search-field{flex:1;background:var(--white);font-size:5.5px;color:#aaa;padding:5px 4px}
.search-btn{width:50px;background:#2f5412;color:#e7f19a;font-weight:700;font-size:7.5px;display:flex;align-items:center;justify-content:center}
.hero-photo{left:62px;top:114px;width:612px;height:302px;background:linear-gradient(110deg,#8bb35a,#e7a0b5 35%,#3c6fb8 60%,#eef3f3 78%,#f4f6f4)}
.date-pill{left:525px;top:182px;width:66px;height:20px;border-radius:10px;background:#c2dc2d;color:#3c5a10;font-size:7px;font-weight:700;display:flex;align-items:center;justify-content:center}
.hero-title{left:520px;top:212px;width:150px;font-family:"Kalam",cursive;font-size:21px;line-height:24px;color:var(--orange)}
.hero-text{left:520px;top:295px;width:140px;font-size:6.5px;line-height:9.8px;color:var(--sky)}
.read-more{left:606px;top:368px;width:46px;height:16px;background:#9ee0f0;color:var(--white);font-size:6.5px;display:flex;align-items:center;justify-content:center}
.donate-ribbon{left:50px;top:318px;width:218px;height:38px;background:#a2c24a;color:var(--white);font-family:"Kalam",cursive;font-size:15px;display:flex;align-items:center;padding-left:24px;clip-path:polygon(0 0,100% 0,94% 100%,0 100%)}
.dot{top:408px;width:13px;height:13px;border-radius:50%;border:2px solid var(--white)}
.side-btn{left:686px;width:59px;height:20px;font-size:6px;font-weight:700;display:flex;align-items:center;justify-content:center}
.tabs{left:62px;top:452px;display:flex;gap:2px}
.tab{width:80px;height:25px;border:1px solid var(--green);border-bottom:none;font-size:6.5px;color:#333;display:flex;align-items:center;justify-content:center;background:var(--white)}
.tab-body{left:62px;top:476px;width:613px;height:185px;border:1px solid var(--green);padding:13px 11px}
.tab-body p{width:402px;font-size:6px;line-height:7.8px;color:var(--muted);margin-bottom:8px}
.photo{background:linear-gradient(135deg,#6b4a33,#c99a73 50%,#4d3a2c)}
.col-head{height:21px;background:linear-gradient(180deg,#5c8c2c,var(--green-dark));color:var(--white);font-size:9.5px;display:flex;align-items:center;padding-left:7px}
.small{font-size:5.5px;line-height:8px;color:#555}
.amount{left:66px;top:742px;width:129px;height:28px;border:1px solid #ddd;display:flex;align-items:center;gap:6px;padding-left:6px;font-size:8px;color:#333;font-weight:700}
.amount b{color:var(--red);font-size:10px}
.donate-btn{left:67px;top:774px;width:126px;height:20px;background:var(--green-dark);color:var(--white);font-weight:700;font-size:9px;display:flex;align-items:center;justify-content:center}
.speaker{left:66px;width:132px;display:flex;gap:6px}
.speaker .thumb{width:28px;height:28px;flex:none}
.speaker p{font-size:5.5px;line-height:7.4px;color:#333}
.speaker i{font-size:4.5px;color:#777}
.mid-box{left:207px;top:679px;width:323px;height:233px;border:1px solid #9bbf5b}
.mid-tabs{display:flex;gap:2px}
.mid-tabs .col-head{padding:0 5px}
.video{left:259px;top:758px;width:219px;height:134px;background:linear-gradient(120deg,#e26a3f,#e8d7b8 45%,#6b7b6a)}
.controls{left:259px;top:880px;width:219px;height:12px;background:#e0e0e0;display:flex;align-items:center;gap:4px;padding:0 6px}
.bar{height:3px;background:#bbb;border-radius:2px}
.gallery{display:grid;grid-template-columns:repeat(4,28px);gap:14px 5px;padding:7px 0 0 6px}
.gallery div{height:28px;border:1px solid #ddd}
.warm{background:linear-gradient(135deg,#5a3a26,#c78a5e)}
.cool{background:linear-gradient(180deg,#e8e8e8,#2e3640)}
.more{width:32px;height:11px;background:var(--green-dark);color:var(--white);font-size:5.5px;display:flex;align-items:center;justify-content:center}
.banner{left:127px;top:946px;width:398px;height:51px;background:linear-gradient(90deg,#333,#777 40%,#c79068 70%,#6b4630);border:1px solid #ccc;color:var(--white);font-size:13px;font-weight:700;display:flex;align-items:center;padding-left:18px;letter-spacing:-.5px}
.badge{left:568px;width:96px;border:1px solid #ccc;background:#f5f5f5}
.skyline{left:66px;top:1028px;width:620px;height:42px;background:linear-gradient(180deg,rgba(185,214,94,0),var(--lime) 40%)}
.footer{left:0;top:1068px;width:745px;height:132px;background:var(--lime)}
.foot-head{font-family:"Amaranth",sans-serif;font-size:18px;color:var(--white)}
.foot-links{list-style:none;font-size:6.5px;font-weight:700;color:var(--white);line-height:14.6px}
.foot-links li::before{content:"→ ";color:var(--green-dark)}
.contact{font-size:6.5px;line-height:9px;color:var(--white)}
.foot-social{width:14px;height:14px;border-radius:50%;background:var(--white)}
.copyright{left:465px;top:1157px;font-size:5px;line-height:7px;color:var(--white)}
</style>
</head>
<body>
<div class="canvas">
  <div class="abs header"></div>
  <div class="abs hero-band"></div>

  <div class="abs live-help">
    <svg width="14" height="14" viewBox="0 0 24 24" aria-hidden="true"><path d="M6.6 10.8a15 15 0 0 0 6.6 6.6l2.2-2.2c.3-.3.7-.4 1-.2 1.1.4 2.3.6 3.6.6.6 0 1 .4 1 1V20c0 .6-.4 1-1 1A17 17 0 0 1 3 4c0-.6.4-1 1-1h3.5c.6 0 1 .4 1 1 0 1.3.2 2.5.6 3.6.1.3 0 .7-.2 1z" fill="#3b6519"/></svg>
    Live Help Online
  </div>
  <div class="abs brand" style="left:265px;top:30px">
    <span class="brand-mark"></span>
    <span>NORTHERN HERITAGE HALL<br>SALLE DU PATRIMOINE DU NORD</span>
  </div>
  <ul class="abs top-links">
    <li>Contact</li><li>Related Sites</li><li>Donate</li><li>Sitemap</li><li>Français</li>
  </ul>
  <div class="abs social" style="left:580px;top:55px"></div>
  <div class="abs social" style="left:612px;top:55px"></div>

  <nav class="abs ribbon" style="left:48px;width:214px;padding-left:22px;clip-path:polygon(0 0,100% 0,100% 100%,0 100%,6% 50%)">
    <svg width="11" height="10" viewBox="0 0 12 10" aria-hidden="true"><path d="M1 5 6 1l5 4M2.5 4v5h7V4" stroke="#fff" fill="none"/></svg>
    <span>ABOUT</span><span>PROJECTS</span><span>SUPPORT PNHH</span>
  </nav>
  <nav class="abs ribbon" style="left:492px;width:203px;padding-left:14px;clip-path:polygon(0 0,100% 0,94% 50%,100% 100%,0 100%)">
    <span>EVENTS</span><span>VOLUNTEERS</span><span>PUBLICATIONS</span>
  </nav>
  <div class="abs search">
    <div class="search-field">Search Your Keyword Here</div>
    <div class="search-btn">SEARCH</div>
  </div>

  <div class="abs hero-photo" role="img" aria-label="Two smiling children holding a cardboard sign reading Give"></div>
  <div class="abs date-pill">04 Aug, 2013</div>
  <h1 class="abs hero-title" style="font-weight:400">Sed do eius-<br>mod tempor<br>incididunt</h1>
  <p class="abs hero-text">Lorem ipsum dolor sit amet conse ctetur adipisicing elit, sed do eiusmod tempor incididunt ut labore et dolore magna aliqua. Ut enim ad minim veniam, quis nostrud exercitation ullamco laboris nisi ut aliquip ex ea commodo consequat. Duis aute irure dolor.</p>
  <div class="abs read-more">Read More</div>
  <div class="abs donate-ribbon">Please Donate for Us</div>
  <div class="abs dot" style="left:562px;background:var(--white)"></div>
  <div class="abs dot" style="left:582px"></div>
  <div class="abs dot" style="left:602px"></div>
  <div class="abs dot" style="left:622px"></div>
  <div class="abs dot" style="left:642px"></div>

  <div class="abs side-btn" style="top:130px;background:#555;color:var(--white)">Meet the Friends</div>
  <div class="abs side-btn" style="top:157px;background:#222;color:var(--white)">Log In <span style="color:#9c3;margin-left:10px">■</span></div>
  <div class="abs" style="left:697px;top:182px;font-size:5.5px;font-style:italic;color:#555">Not a Member?</div>

  <div class="abs tabs">
    <div class="tab">BE A FRIEND</div><div class="tab">BE A DONOR</div><div class="tab">BE A VOLUNTEER</div>
  </div>
  <div class="abs tab-body">
    <p>Lorem ipsum dolor sit amet, consectetur adipiscing elit. Sed blandit massa vel mauris sollicitudin dignissim. Phasellus ultrices tellus eget ipsum ornare molestie scelerisque eros dignissim. Phasellus fringilla hendrerit lectus nec vehicula.</p>
    <p>Pellentesque habitant morbi tristique senectus et netus et malesuada fames ac turpis egestas. In faucibus, risus eu volutpat pellentesque, massa felis feugiat velit, nec mattis felis elit a eros.</p>
    <p>Cras convallis sodales orci, et pretium sapien egestas quis. Donec tellus leo, scelerisque in facilisis a, laoreet vel quam. Suspendisse arcu nisl, tincidunt a vulputate ac, feugiat vitae leo. Integer hendrerit orci id metus venenatis in luctus.</p>
    <p>Lorem ipsum dolor sit amet, consectetur adipiscing elit. Sed blandit massa vel mauris sollicitudin dignissim. Phasellus ultrices tellus eget ipsum ornare molestie scelerisque eros dignissim. Phasellus fringilla hendrerit lectus nec vehicula.</p>
    <p>Pellentesque habitant morbi tristique senectus et netus et malesuada fames ac turpis egestas. In faucibus, risus eu volutpat pellentesque, massa felis feugiat velit, nec mattis felis elit a eros.</p>
    <p>Cras convallis sodales orci, et pretium sapien egestas quis. Donec tellus leo, scelerisque in facilisis a, laoreet vel quam. Suspendisse arcu nisl, tincidunt a vulputate ac, feugiat vitae leo. Integer hendrerit orci id metus venenatis in luctus.</p>
    <p>Cras convallis sodales orci, et pretium sapien egestas quis. Donec tellus leo, scelerisque in facilisis a, laoreet vel quam. Suspendisse arcu nisl, tincidunt a vulputate ac, feugiat vitae leo. Integer hendrerit orci id metus venenatis in luctus.</p>
  </div>
  <div class="abs photo" style="left:483px;top:507px;width:184px;height:120px;border:1px solid #ddd" role="img" aria-label="Two young children resting together"></div>

  <div class="abs" style="left:62px;top:679px;width:136px">
    <div class="col-head">BECOME A VOLUNTEER</div>
    <p class="small" style="padding:8px 6px">Lorem ipsum dolor sit amet, consectetur adipiscing elit Nam pulvinar.</p>
  </div>
  <div class="abs amount"><b>$2,500</b> Target, $25,000</div>
  <div class="abs donate-btn">DONATE NOW</div>
  <div class="abs col-head" style="left:62px;top:808px;width:136px">SPEAKER'S BUREAU</div>
  <div class="abs speaker" style="top:835px">
    <div class="thumb warm" role="img" aria-label="Speaker portrait"></div>
    <p>Class aptent taciti sociosqu ad litora torquent<br><i>March 26, 2012, 0 comments</i></p>
  </div>
  <div class="abs" style="left:62px;top:870px;width:136px;border-top:1px solid #eee"></div>
  <div class="abs speaker" style="top:877px">
    <div class="thumb cool" role="img" aria-label="Speaker portrait"></div>
    <p>Cras vel hendrerit leo. Integer tortor leo<br><i>March 26, 2012, 0 comments</i></p>
  </div>

  <div class="abs mid-box"></div>
  <div class="abs mid-tabs" style="left:207px;top:679px">
    <div class="col-head">NEW EVENTS</div><div class="col-head">ANNOUNCEMENTS</div><div class="col-head" style="width:150px">CROWD SOURCING PROJECTS</div>
  </div>
  <div class="abs" style="left:219px;top:710px;width:297px;font-size:7px;color:#333;display:flex;justify-content:space-between">
    <span>Lorem ipsum dolor sit amet conse</span><span style="font-size:6px">Aug 14, <span style="color:var(--red)">2013</span></span>
  </div>
  <p class="abs" style="left:219px;top:724px;width:297px;font-size:6px;line-height:9px;color:var(--muted)">Arenean nonummy hendrerit mau phaselntes nascetur ridic ulusm dui fusce feu. Cras vitae neque turpis, in luctus risus.... <b style="color:var(--green)">&gt;</b></p>
  <div class="abs" style="left:219px;top:749px;width:297px;border-top:1px dashed #e2e2e2"></div>
  <div class="abs video" role="img" aria-label="Video still of two men sharing a meal at a café"></div>
  <div class="abs controls">
    <span style="font-size:6px;color:#555">▶</span>
    <div class="bar" style="width:110px;background:linear-gradient(90deg,var(--red) 60%,#bbb 60%)"></div>
    <span style="font-size:4px;color:#777">3:47 / 8:29</span>
    <span style="font-size:6px;color:#555">◀</span>
    <div class="bar" style="width:26px"></div>
  </div>

  <div class="abs" style="left:538px;top:679px;width:136px">
    <div class="col-head">PHOTO GALLERY</div>
    <div class="gallery" role="img" aria-label="Gallery thumbnails">
      <div class="warm"></div><div class="warm"></div><div class="warm"></div><div class="warm"></div>
      <div class="cool"></div><div class="cool"></div><div class="cool"></div><div class="cool"></div>
    </div>
  </div>
  <div class="abs more" style="left:592px;top:791px">More</div>
  <div class="abs" style="left:538px;top:808px;width:136px">
    <div class="col-head">MEMBER TREASURES</div>
    <div class="gallery" role="img" aria-label="Member treasure thumbnails">
      <div class="warm"></div><div class="warm"></div><div class="warm"></div><div class="warm"></div>
      <div class="cool"></div><div class="cool"></div><div class="cool"></div><div class="cool"></div>
    </div>
  </div>
  <div class="abs more" style="left:592px;top:920px">More</div>

  <div class="abs banner" role="img" aria-label="Banner photo of smiling children">Share Happiness Banner 728x90</div>
  <div class="abs badge" style="top:944px;height:30px"></div>
  <div class="abs badge" style="top:988px;height:32px"></div>

  <div class="abs skyline" role="img" aria-label="City skyline silhouette"></div>
  <footer class="abs footer">
    <h2 class="abs foot-head" style="left:105px;top:6px;font-weight:400">Navigation</h2>
    <ul class="abs foot-links" style="left:110px;top:34px">
      <li>HOME</li><li>ABOUT US</li><li>SUPPORT PNHH</li><li>PROJECTS</li><li>EVENTS</li><li>VOLUNTEERS</li>
    </ul>
    <ul class="abs foot-links" style="left:187px;top:34px">
      <li>PUBLICATIONS</li><li>MEET THE FRIENDS</li>
    </ul>
    <h2 class="abs foot-head" style="left:298px;top:6px;font-weight:400">Quick Contact</h2>
    <div class="abs contact" style="left:304px;top:38px">48 Larchfield Row<br>Northvale &nbsp;NV 2210<br><br>T: +41 555 0186<br>M: 0555 019 742<br><br>www.patrons-hall.org</div>
    <div class="abs brand" style="left:466px;top:35px;font-size:7.5px;line-height:9px">
      <span class="brand-mark"></span>
      <span>NORTHERN HERITAGE HALL<br>SALLE DU PATRIMOINE DU NORD</span>
    </div>
    <div class="abs foot-social" style="left:525px;top:68px"></div>
    <div class="abs foot-social" style="left:543px;top:68px"></div>
    <div class="abs foot-social" style="left:561px;top:68px"></div>
  </footer>
  <p class="abs copyright">Copyright 2013 Patrons of the Northern Heritage Hall.<br>All Rights Reserved, Harbour Lane, Northvale NV 2210</p>
</div>
</body>
</html>
```